Small Business Consulting Firm Needs Business Card Design

Need a sleek modern business card with 2 sides matching the colors of our logo. We will be placing these with a mailer we are sending out. These business cards will only ever be given to business owners. We operate helping businesses who are struggling with cash flow or finances. If the green and blue design needs to be moved to the right of "Harborline Crest Consulting" for aesthetic purposes that is ok. We will need an editable file if possible. We would like to include the reps name, email, website, and phone number. For now just use Peter Vance, pvance@harborlinecrest.com, www.harborlinecrest.com, and 833-555-0172.

```html
<!DOCTYPE html>
<html lang="en">
<head>
<meta charset="utf-8">
<title>Harborline Crest Consulting – Business Card</title>
<link rel="stylesheet" href="https://fonts.googleapis.com/css2?family=Open+Sans:wght@400&display=swap">
<style>
  :root {
    --backdrop: #bcbdbf;
    --card: #ffffff;
    --tone-blue: #7aafdd;
    --tone-teal: #58a5b2;
    --tone-green: #bcd99c;
    --brand-green: #76b843;
    --ink: #444446;
  }
  html, body {
    margin: 0;
    width: 1200px;
    height: 849px;
    overflow: hidden;
    background: var(--backdrop);
  }
  .card {
    position: absolute;
    top: 266px;
    width: 501px;
    height: 286px;
    background: var(--card);
    box-shadow: 0 0 0 1px rgba(0,0,0,0.25);
  }
  .card--front { left: 91px; }
  .card--back { left: 626px; }
  .card svg { display: block; width: 100%; height: 100%; }
  .stop-blue { stop-color: var(--tone-blue); }
  .stop-teal { stop-color: var(--tone-teal); }
  .stop-green { stop-color: var(--tone-green); }
  .stop-white { stop-color: var(--card); }
  .brand-mark { fill: var(--brand-green); }
  .type {
    font-family: "Open Sans", "Segoe UI", sans-serif;
    font-weight: 400;
    fill: var(--ink);
  }
</style>
</head>
<body>

<svg width="0" height="0" style="position:absolute" aria-hidden="true">
  <defs>
    <linearGradient id="tone-sweep" x1="0" y1="0" x2="1" y2="0">
      <stop offset="0" class="stop-blue"/>
      <stop offset="0.5" class="stop-teal"/>
      <stop offset="1" class="stop-green"/>
    </linearGradient>
    <linearGradient id="white-fade" x1="0" y1="0" x2="0" y2="1">
      <stop offset="0" class="stop-white" stop-opacity="1"/>
      <stop offset="0.55" class="stop-white" stop-opacity="0.35"/>
      <stop offset="1" class="stop-white" stop-opacity="0"/>
    </linearGradient>
  </defs>
</svg>

<div class="card card--front">
  <svg viewBox="0 0 733 418" aria-label="Front of card">
    <g class="backdrop-field" role="img" aria-label="Decorative background area in soft blue, teal and green">
      <rect x="0" y="99" width="733" height="319" fill="url(#tone-sweep)"/>
      <rect x="0" y="99" width="733" height="220" fill="url(#white-fade)"/>
    </g>

    <rect class="brand-mark" x="321" y="95" width="90" height="90"/>
    <text class="type brand-name" x="366" y="261" text-anchor="middle" font-size="36" letter-spacing="1">HARBORLINE CREST</text>
    <text class="type brand-tagline" x="366" y="292" text-anchor="middle" font-size="19" letter-spacing="11">CONSULTING</text>
  </svg>
</div>

<div class="card card--back">
  <svg viewBox="0 0 733 418" aria-label="Back of card">
    <g class="backdrop-field" role="img" aria-label="Decorative background area in soft blue, teal and green">
      <rect x="0" y="99" width="733" height="319" fill="url(#tone-sweep)"/>
      <rect x="0" y="99" width="733" height="220" fill="url(#white-fade)"/>
    </g>

    <rect class="brand-mark" x="638" y="14" width="32" height="32"/>
    <text class="type brand-name" x="654" y="65" text-anchor="middle" font-size="12">HARBORLINE CREST</text>
    <text class="type brand-tagline" x="654" y="76" text-anchor="middle" font-size="6" letter-spacing="3.5">CONSULTING</text>

    <text class="type rep-name" x="366" y="128" text-anchor="middle" font-size="34" letter-spacing="1.5">Peter Vance</text>

    <text class="type contact" x="720" y="272" text-anchor="end" font-size="19" letter-spacing="1">pvance@harborlinecrest.com</text>
    <text class="type contact" x="720" y="307" text-anchor="end" font-size="19" letter-spacing="1">www.harborlinecrest.com</text>
    <text class="type contact" x="720" y="339" text-anchor="end" font-size="19" letter-spacing="1">833-555-0172</text>
  </svg>
</div>

</body>
</html>
```